Refresh of The Marston Collective business card

Update business card design using existing primary logo. Names, numbers, etc. are too hard to read on current design.

Target Market(s)

We are a CPA firm.

Industry/Entity Type

Accountant

Contact Information for Business Card

update current card

Colors
0355a3
3176b5
85acd3
0792cd

Requirements
Must have
• Easier to read phone numbers and names
• Use existing logo
Nice to have
• We love our color scheme and current TMC logo. But the names and phone numbers are too small and card just look old and stale.

```html
<!DOCTYPE html>
<html lang="en">
<head>
<meta charset="utf-8">
<title>The Marston Collective – Business Card</title>
<link href="https://fonts.googleapis.com/css2?family=Cinzel:wght@500&family=Montserrat:wght@500;600&family=Cormorant+SC:wght@600&display=swap" rel="stylesheet">
<style>
  :root {
    --navy: #0355a3;
    --mid-blue: #3176b5;
    --light-blue: #85acd3;
    --bright-blue: #0792cd;
    --card-blue-deep: #0a72bb;
    --card-blue-glow: #3aa1da;
    --white: #ffffff;
    --ink: #1b1b1b;
    --backdrop: #eceef1;
  }
  * { margin: 0; padding: 0; box-sizing: border-box; }
  html, body { width: 1200px; height: 1000px; overflow: hidden; }
  body { background: var(--backdrop); position: relative; font-family: "Montserrat", sans-serif; }

  .card { position: absolute; box-shadow: 0 4px 10px rgba(0,0,0,.25); overflow: hidden; }

  /* Front */
  .card-front {
    left: 183px; top: 22px; width: 793px; height: 455px;
    background: radial-gradient(ellipse 55% 70% at 57% 58%, var(--card-blue-glow) 0%, var(--card-blue-deep) 100%);
  }
  .front-mark {
    position: absolute; left: 108px; top: 122px; width: 160px; height: 160px;
    border: 4px solid var(--white); border-radius: 50%;
  }
  .front-name {
    position: absolute; left: 292px; top: 128px;
    font-family: "Cinzel", serif; font-weight: 500; color: var(--white);
    font-size: 46px; line-height: 50px; letter-spacing: 1px;
  }
  .front-tagline {
    position: absolute; left: 294px; top: 266px;
    font-family: "Montserrat", sans-serif; font-weight: 600; color: var(--white);
    font-size: 12px; letter-spacing: 2.6px;
  }
  .front-web {
    position: absolute; left: 0; right: 0; top: 384px; text-align: center; padding-left: 90px;
    font-weight: 600; font-size: 14px; color: var(--white);
  }

  /* Back */
  .card-back { left: 181px; top: 497px; width: 795px; height: 453px; background: var(--white); }
  .band { position: absolute; left: 0; width: 100%; background: linear-gradient(90deg, var(--mid-blue), var(--bright-blue)); }
  .band-top { top: 0; height: 30px; }
  .band-bottom { bottom: 0; height: 37px; }

  .back-logo { position: absolute; left: 66px; top: 50px; display: flex; align-items: center; gap: 8px; }
  .back-mark { width: 50px; height: 50px; border-radius: 50%; background: var(--navy); border: 2px solid var(--light-blue); }
  .back-name { font-family: "Cinzel", serif; font-weight: 500; color: var(--navy); font-size: 15px; line-height: 16px; }
  .back-tagline { font-size: 5px; letter-spacing: 1px; color: var(--navy); margin-top: 2px; font-weight: 600; }

  .person-name {
    position: absolute; left: 62px; top: 222px;
    font-family: "Cormorant SC", serif; font-weight: 600; font-size: 30px; color: var(--ink);
  }

  .contact-list { position: absolute; left: 502px; top: 156px; list-style: none; }
  .contact-item { display: flex; align-items: flex-start; gap: 18px; font-weight: 600; font-size: 14px; color: var(--ink); line-height: 20px; }
  .contact-item svg { width: 18px; height: 18px; flex: none; margin-top: 1px; fill: var(--mid-blue); }
  .contact-address { margin-bottom: 18px; text-align: center; }
  .contact-item + .contact-item { margin-top: 16px; }
  .contact-email { margin-top: 21px !important; }
</style>
</head>
<body>

<section class="card card-front">
  <div class="front-mark"></div>
  <div class="front-name">The Marston<br>Collective</div>
  <div class="front-tagline">CERTIFIED PUBLIC ACCOUNTANTS</div>
  <div class="front-web">www.themarstoncollective.com</div>
</section>

<section class="card card-back">
  <div class="band band-top"></div>

  <div class="back-logo">
    <div class="back-mark"></div>
    <div>
      <div class="back-name">The Marston<br>Collective</div>
      <div class="back-tagline">CERTIFIED PUBLIC ACCOUNTANTS</div>
    </div>
  </div>

  <div class="person-name">Daniel R. Marston, CPA</div>

  <ul class="contact-list">
    <li class="contact-item contact-address">
      <svg viewBox="0 0 20 20" aria-hidden="true"><circle cx="10" cy="10" r="9" fill="none" stroke="#3176b5" stroke-width="1.6"/><ellipse cx="10" cy="10" rx="4" ry="9" fill="none" stroke="#3176b5" stroke-width="1.4"/><path d="M1 10h18M3 5h14M3 15h14" stroke="#3176b5" stroke-width="1.2"/></svg>
      <span>218 W. Harbor Ln . Suite 104<br>Ashford, Florida 32900</span>
    </li>
    <li class="contact-item">
      <svg viewBox="0 0 20 20" aria-hidden="true"><path d="M4 1.5l3.5 3-1.8 2.6c1 2.4 2.8 4.3 5.2 5.4l2.6-1.8 3 3.5-2.3 2.6C8.5 16.3 3.2 11 2 3.8z"/></svg>
      <span>555 .014 .2290</span>
    </li>
    <li class="contact-item">
      <svg viewBox="0 0 20 20" aria-hidden="true"><rect x="2" y="3" width="5" height="15" rx="1.5"/><rect x="8" y="6" width="10" height="12" rx="1.5"/><rect x="9" y="1.5" width="7" height="4" fill="#85acd3"/></svg>
      <span>555 .014 .2291</span>
    </li>
    <li class="contact-item">
      <svg viewBox="0 0 20 20" aria-hidden="true"><rect x="5" y="1" width="10" height="18" rx="2"/><rect x="7" y="3.5" width="6" height="10" fill="#ffffff"/></svg>
      <span>555 .014 .2292</span>
    </li>
    <li class="contact-item contact-email">
      <svg viewBox="0 0 20 20" aria-hidden="true"><rect x="1" y="4" width="18" height="12" rx="1"/><path d="M1.5 4.8L10 11l8.5-6.2" fill="none" stroke="#ffffff" stroke-width="1.5"/></svg>
      <span>dan@themarstoncollective.com</span>
    </li>
  </ul>

  <div class="band band-bottom"></div>
</section>

</body>
</html>
```